New landing page for book

Redesign http://www.kelvostramedia.com so it looks more cutting edge and perhaps have buttons for the online bookstores.

Also I may soon have a trailer video produced so it Would be great to see an option with space for where a video might go and an option as the site is now without a video. Thanks

Industry/Entity Type

Online

Number of Pages Required

1 page

Colors

Designer to choose colors to be used in the design.

```html
<!DOCTYPE html>
<html lang="en">
<head>
<meta charset="utf-8">
<title>Velgrada – International Financial Crime Thriller</title>
<link href="https://fonts.googleapis.com/css2?family=Oswald:wght@500;600;700&family=Roboto+Condensed:wght@400;700&display=swap" rel="stylesheet">
<style>
:root{
  --ink:#1b1a19;
  --nav:#231d1a;
  --hero-a:#6b4a35;
  --hero-b:#2a1612;
  --brown:#4a2420;
  --orange:#ec6a2c;
  --teal-dark:#1d4a44;
  --mint:#b2e0cd;
  --mint-fade:#6f978a;
  --wall:#14211f;
  --white:#ffffff;
  --text:#5a3a33;
  --footer:#0c0f0e;
}
*{margin:0;padding:0;box-sizing:border-box}
html,body{width:1105px;height:1200px;overflow:hidden}
body{position:relative;background:var(--white);font-family:"Roboto Condensed",sans-serif;color:var(--text)}
.hero{position:absolute;left:0;top:0;width:1105px;height:394px;background:linear-gradient(90deg,#7a5238 0%,var(--hero-a) 20%,#3d2119 60%,var(--hero-b) 100%)}
.topbar{position:absolute;left:0;top:21px;width:1105px;height:46px;background:var(--nav);opacity:.95}
.site-title{position:absolute;left:139px;top:34px;font-family:"Oswald",sans-serif;font-weight:600;font-size:17px;color:var(--white);letter-spacing:.2px;text-transform:uppercase}
.nav{position:absolute;right:173px;top:34px;display:flex;gap:14px;font-family:"Oswald",sans-serif;font-weight:600;font-size:17px;color:var(--white);text-transform:uppercase}
.nav .caret{font-size:9px;vertical-align:top;margin-left:6px}
.cover{position:absolute;left:138px;top:94px;width:217px;height:342px;background:linear-gradient(180deg,#3b2c24 0%,#8a5a2c 35%,#2f4a3f 75%,#1f3a34 100%)}
.buy-band{position:absolute;left:138px;top:436px;width:217px;height:56px;background:var(--teal-dark);color:var(--white);font-family:"Oswald",sans-serif;font-weight:700;font-size:38px;text-align:center;line-height:56px}
.stores{position:absolute;left:138px;top:504px;width:217px;display:grid;grid-template-columns:103px 103px;gap:11px 11px}
.store{height:46px;border:1px solid #c9c9c9;background:var(--white);display:flex;align-items:center;justify-content:center;gap:6px;font-family:"Roboto Condensed",sans-serif;font-weight:700;font-size:15px;color:#333}
.store .dot{width:10px;height:10px;border-radius:50%;background:#9a9a9a}
.video{position:absolute;left:405px;top:93px;width:517px;height:284px;background:var(--ink)}
.video svg{position:absolute;left:0;top:0}
.headline{position:absolute;left:384px;top:420px;width:540px;font-family:"Oswald",sans-serif;font-weight:500;font-size:23px;line-height:25px;color:var(--brown);text-transform:uppercase}
.headline .title{color:var(--orange)}
.synopsis{position:absolute;left:384px;top:515px;width:540px;font-size:9.4px;line-height:12px;color:var(--text)}
.synopsis p{margin-bottom:11px}
.synopsis .lead{font-weight:700;font-size:11px;line-height:13px;color:var(--brown)}
.reviews{position:absolute;left:0;top:734px;width:1105px;height:419px;background:radial-gradient(ellipse at 50% 40%,#22332f 0%,var(--wall) 70%,#0e1614 100%)}
.reviews h2{position:absolute;left:0;width:1105px;top:50px;text-align:center;font-family:"Oswald",sans-serif;font-weight:700;font-size:38px;color:var(--white)}
.card{position:absolute;text-align:center}
.card-side{top:152px;height:158px;background:var(--mint-fade);opacity:.85;overflow:hidden;color:#23302c;font-size:9.5px;line-height:14px}
.card-left{left:138px;width:218px}
.card-right{left:749px;width:217px}
.card-side .quote{position:absolute;top:52px;width:360px}
.card-left .quote{left:34px;text-align:left}
.card-right .quote{right:34px;text-align:right}
.card-side .who{position:absolute;top:117px;font-weight:700;font-size:9.5px}
.card-left .who{left:135px}
.card-right .who{left:12px}
.card-main{left:356px;top:133px;width:393px;height:183px;background:var(--mint);color:#2e4a43}
.card-main .quote{position:absolute;left:50px;top:62px;width:293px;font-size:11px;line-height:16.5px}
.card-main .mark{font-family:"Oswald",sans-serif;font-weight:700;font-size:16px;color:#2e4a43}
.card-main .who{position:absolute;left:0;width:393px;top:133px;font-weight:700;font-size:11px}
.bubble{position:absolute;left:512px;top:110px}
.dots{position:absolute;left:516px;top:348px;display:flex;gap:9px}
.dots span{width:12px;height:12px;border-radius:50%;background:#5fb59a}
.dots span.on{background:transparent;border:1.5px solid var(--white)}
.footer{position:absolute;left:0;top:1153px;width:1105px;height:47px;background:var(--footer);color:#c9c9c9;font-size:8px;text-align:center;line-height:47px;text-transform:uppercase}
.to-top{position:absolute;left:918px;top:1142px;width:37px;height:37px;border-radius:50%;background:#3a3a3a}
</style>
</head>
<body>
<header class="hero"></header>
<div class="topbar"></div>
<div class="site-title">International Financial Crime Thriller</div>
<nav class="nav"><span>Buy Now<span class="caret">▼</span></span><span>Contact</span></nav>

<div class="cover" role="img" aria-label="Book cover of Velgrada by Marek Halloway: a man with a handgun in front of the Capitol dome under a stormy sky"></div>
<div class="buy-band">BUY NOW!</div>

<div class="stores">
  <div class="store"><span class="dot"></span>Brightshelf</div>
  <div class="store">Harrow &amp; Finch</div>
  <div class="store"><span class="dot"></span>Pagewell</div>
  <div class="store"><span class="dot"></span>Leafstand</div>
  <div class="store"><span class="dot"></span>Quillo</div>
  <div class="store">Inkrunner</div>
</div>

<div class="video">
  <svg width="517" height="284" viewBox="0 0 517 284">
    <circle cx="263" cy="133" r="37" fill="none" stroke="#fff" stroke-width="3"/>
    <polygon points="252,115 252,151 283,133" fill="#fff"/>
    <rect x="11" y="267" width="494" height="4" rx="2" fill="#5a5a5a"/>
    <circle cx="23" cy="269" r="6" fill="#d8d8d8"/>
  </svg>
</div>

<h1 class="headline"><span class="title">Velgrada:</span> ATMs have shuttered. Stock markets have gone haywire. Can one operative stop a deadly band of criminals before it is too late?</h1>

<div class="synopsis">
  <p class="lead">When Anton Reiser is asked to investigate a devastating cyber-attack, he is drawn into a conspiracy that threatens not only his own life, but the entire United States’ economy...</p>
  <p>German intelligence operative Anton Reiser has been asked to investigate the cyber crime gang who sparked massive unrest in Kenya by taking over electronic transactions. But as he digs deeper, a wiretap on hacker communications reveals this is only the beginning.</p>
  <p>Velgrada, a shadowy criminal cabal, has launched a massive cyber attack on the United States.</p>
  <p>Taking off for Washington, Reiser unexpectedly teams up with American gun for hire, Dale Kessinger, and dives head-first into a massive conspiracy that reaches all the way up to the very top of the U.S. Government.</p>
  <p>Stock markets have gone haywire. ATMs have shuttered. And Anton Reiser is about to come face to face with the men he is sent to find....</p>
  <p class="lead">From the deadly streets of Budapest to the equally perilous corridors of Washington, Velgrada is an action-packed, compulsive thriller that depicts a financial scam terrifyingly close to reality.</p>
</div>

<section class="reviews">
  <h2>WHAT PEOPLE SAY</h2>
  <div class="card card-side card-left">
    <p class="quote">In a world ravaged by international turmoil and uncertainty for the future,<br>author Marek Halloway presents Velgrada, an intense and politically charged<br>novel that is both timely and terrifying.”</p>
    <p class="who">- Celia Norwand -</p>
  </div>
  <div class="card card-side card-right">
    <p class="quote">In a world ravaged by international turmoil and uncertainty for the future,<br>author Marek Halloway presents Velgrada, an intense and politically charged<br>novel that is both timely and terrifying.”</p>
    <p class="who">- Celia Norwand -</p>
  </div>
  <div class="card card-main">
    <p class="quote"><span class="mark">“</span> I give Velgrada by Marek Halloway a definite four out of four stars. The action is fast paced so that it keeps you wanting to see what comes next. <span class="mark">”</span></p>
    <p class="who">- ReadingCircleHub -</p>
  </div>
  <svg class="bubble" width="80" height="58" viewBox="0 0 80 58">
    <path d="M30 4 C12 4 4 14 4 24 C4 31 8 36 13 39 L8 49 L22 42 C25 43 28 43 30 43" fill="none" stroke="#5fb59a" stroke-width="3.5"/>
    <ellipse cx="50" cy="32" rx="27" ry="19" fill="#5fb59a"/>
    <path d="M60 47 L70 56 L66 44 Z" fill="#5fb59a"/>
    <rect x="36" y="27" width="28" height="2" fill="#b2e0cd"/>
    <rect x="36" y="32" width="28" height="2" fill="#b2e0cd"/>
    <rect x="36" y="37" width="28" height="2" fill="#b2e0cd"/>
  </svg>
  <div class="dots"><span></span><span class="on"></span><span></span><span></span></div>
</section>

<footer class="footer">© Copyright 2017 Marek Halloway - All Rights Reserved</footer>
<svg class="to-top" width="37" height="37" viewBox="0 0 37 37">
  <circle cx="18.5" cy="18.5" r="18.5" fill="#3a3a3a"/>
  <path d="M18.5 27 V11 M13.5 16 L18.5 10.5 L23.5 16" fill="none" stroke="#fff" stroke-width="2"/>
</svg>
</body>
</html>
```